Letterhead for a German Distribution/Manufacturing Company

We need a professional Letterhead in a unique Design.
not to playful.
The Letterhead has to show show that we are a international company with headquater in Germany.
all details like adress, Vat Tax Number, Bank Accout, Eori, email, Company number has to be on the Letterhead.
for example use: VAT TAX DE5704168 Bank Account: Norrfeld Bank IBAN DE421705238ß310482 Swift: KOLV3154802 EORI 3041296587 Company Number: HRB 61508 Adress: VOLTRINA UG Amsel Strasse 7 Postal Code 04683 City Lindenhain Country: Germany Email: info@voltrina-example.com
the design can be colored but doesnt have to be
Industry/Entity Type
Manufacturing and international distribution
Requirements
Must have
- show that we are a international company with headquater in Germany. our company infos and logo

```html
<!DOCTYPE html>
<html lang="en">
<head>
<meta charset="utf-8">
<title>VOLTRINA UG – Letterhead</title>
<link rel="stylesheet" href="https://fonts.googleapis.com/css2?family=Open+Sans:wght@400&family=Roboto:wght@400;500&display=swap">
<style>
  :root {
    --backdrop: #dedede;
    --paper: #f8f8f8;
    --ink-dark: #424242;
    --ink-body: #666666;
    --ink-meta: #4a4a4a;
    --signature-tone: #d5d8de;
  }
  * { margin: 0; padding: 0; box-sizing: border-box; }
  html, body {
    width: 1153px; height: 1200px; overflow: hidden;
    background: var(--backdrop);
  }
  .letterhead {
    position: absolute; left: 167px; top: 30px;
    width: 818px; height: 1140px;
    background: var(--paper);
    box-shadow: 0 14px 30px rgba(0,0,0,0.14);
  }
  .brand {
    position: absolute; left: 81px; top: 70px;
    display: flex; align-items: center; gap: 14px;
  }
  .brand-dot {
    width: 66px; height: 66px; border-radius: 50%;
    background: var(--ink-dark);
  }
  .brand-name {
    font-family: "Open Sans", sans-serif; font-weight: 400;
    font-size: 48px; letter-spacing: 0.5px; color: var(--ink-dark);
  }
  .sender {
    position: absolute; left: 577px; top: 60px;
    font-family: "Roboto", sans-serif; font-size: 14px; line-height: 17.5px;
    color: var(--ink-meta); font-style: normal;
  }
  .sender-contacts { list-style: none; margin-top: 6px; }
  .sender-contacts li { display: flex; align-items: center; gap: 7px; line-height: 18px; }
  .sender-contacts svg { width: 13px; height: 13px; fill: var(--ink-meta); }
  .letter-body {
    position: absolute; left: 81px; top: 278px; width: 656px;
    font-family: "Open Sans", sans-serif; font-size: 14.9px; line-height: 21.6px;
    color: var(--ink-body);
  }
  .letter-body p { margin-bottom: 21.6px; text-align: justify; }
  .letter-body .salutation, .letter-body .closing { text-align: left; }
  .signature {
    position: absolute; left: 81px; top: 846px; width: 94px; height: 88px;
    background: var(--signature-tone); border-radius: 4px;
  }
  .company-register {
    position: absolute; left: 81px; top: 1036px;
    font-family: "Roboto", sans-serif; font-size: 13.6px; line-height: 19px;
    color: var(--ink-meta);
  }
  .company-register .divider { font-weight: 500; padding: 0 2px; }
</style>
</head>
<body>
  <main class="letterhead">
    <header>
      <div class="brand">
        <span class="brand-dot"></span>
        <span class="brand-name">VOLTRINA</span>
      </div>
      <address class="sender">
        <div>VOLTRINA UG</div>
        <div>Amsel Strasse 7 04683</div>
        <div>City Lindenhain Germany</div>
        <ul class="sender-contacts">
          <li>
            <svg viewBox="0 0 16 16" aria-hidden="true"><path d="M2 5c0-1.5 2.5-3 6-3s6 1.5 6 3v1.5h-3.5V5h-5v1.5H2z M4 8h8l2 5H2z M8 9.3a1.6 1.6 0 1 0 0 3.2a1.6 1.6 0 1 0 0-3.2z"/></svg>
            555.204.7163
          </li>
          <li>
            <svg viewBox="0 0 16 16" aria-hidden="true"><path d="M1 3h14v1.5L8 9L1 4.5z M1 6.3l7 4.5l7-4.5V13H1z"/></svg>
            info@voltrina-example.com
          </li>
          <li>
            <svg viewBox="0 0 16 16" aria-hidden="true"><circle cx="8" cy="8" r="7"/><path d="M5 4c2 0 3 1 2 2.5S5 7 5 9s2 2 2 4" stroke="#f8f8f8" stroke-width="1.4" fill="none"/></svg>
            www.voltrina-example.com
          </li>
        </ul>
      </address>
    </header>

    <section class="letter-body">
      <p class="salutation">Dear customer,</p>
      <p>Lorem ipsum dolor sit amet, consectetur adipisicing elit, sed do eiusmod tempor incididunt ut labore et dolore magna aliqua. Ut enim ad minim veniam, quis nostrud exercitation ullamco laboris nisi ut aliquip ex ea commodo consequat. Duis aute irure dolor in reprehenderit in voluptate velit esse cillum dolore eu fugiat nulla pariatur. Excepteur sint occaecat cupidatat non proident, sunt in culpa qui officia deserunt mollit anim id est laborum.</p>
      <p>Lorem ipsum dolor sit amet, consectetur adipisicing elit, sed do eiusmod tempor incididunt ut labore et dolore magna aliqua. Ut enim ad minim veniam, quis nostrud exercitation ullamco laboris nisi ut aliquip ex ea commodo consequat. Duis aute irure dolor in reprehenderit in voluptate velit esse cillum dolore eu fugiat nulla pariatur. Excepteur sint occaecat cupidatat non proident, sunt in culpa qui officia deserunt mollit anim id est laborum.</p>
      <p>Lorem ipsum dolor sit amet, consectetur adipisicing elit, sed do eiusmod tempor incididunt ut labore et dolore magna aliqua. Ut enim ad minim veniam, quis nostrud exercitation ullamco laboris nisi ut aliquip ex ea commodo consequat. Duis aute irure dolor in reprehenderit in voluptate velit esse cillum dolore eu fugiat nulla pariatur. Excepteur sint occaecat cupidatat non proident, sunt in culpa qui officia deserunt mollit anim id est laborum.</p>
      <p>Lorem ipsum dolor sit amet, consectetur adipisicing elit, sed do eiusmod tempor incididunt ut labore et dolore magna aliqua. Ut enim ad minim veniam, quis nostrud exercitation ullamco laboris nisi ut aliquip ex ea commodo consequat. Duis aute irure dolor in reprehenderit.</p>
      <p class="closing">Yours Sincerely,</p>
    </section>

    <div class="signature" role="img" aria-label="Handwritten signature of the sender"></div>

    <footer class="company-register">
      <div>VAT TAX DE5704168</div>
      <div>Bank Account: Norrfeld Bank IBAN DE421705238ß310482</div>
      <div>Swift: KOLV3154802 EORI 3041296587 <span class="divider">|</span> Company Number: HRB 61508</div>
    </footer>
  </main>
</body>
</html>
```